Lease-My-Goose's web page

I need a web page(s) to show and promote my business of renting chickens. We provide seasonal rentals in the United States of a layer hen package for people who would like to try raising their own chickens. The package includes two hens, coop, attached run, feeder, waterer, and food. I would like interested people to be able to fill out a form so that I can have partners contact them to set up a delivery in their area. Our service is very popular with urban and suburban families.

Target Market(s)

Urban foodies.
Families.
People interested in Organic Foods.
People concerned with where their food comes from and how it is grown/prepared.
People interested in Urban Farming.

Industry/Entity Type

Business

Requirements
Must have
• A way for me to see rental interest based on zip code.
• A contact form including zip code, e-mail, and optional phone number.
• Our Logo. (Please contact if you are unable to use the file I provided.)
Nice to have
• A guest book for former renters that we can vet before posting.

```html
<!DOCTYPE html>
<html lang="en">
<head>
<meta charset="utf-8">
<title>Lease-My-Goose</title>
<link href="https://fonts.googleapis.com/css2?family=PT+Sans:wght@400;700&family=Roboto+Condensed:wght@500;700&display=swap" rel="stylesheet">
<style>
:root{
  --sky-bottom:#cdeefa;
  --red:#e1251b;
  --red-dark:#b7160f;
  --yellow:#fbd92b;
  --yellow-deep:#f3c21c;
  --green-title:#76a325;
  --text:#6b6b6b;
  --heading:#2d2d2d;
  --maroon:#8f1d10;
  --footer-bg:#eaf6fb;
  --footer-link:#4d7f94;
  --white:#ffffff;
}
*{margin:0;padding:0;box-sizing:border-box}
html,body{width:1055px;height:1200px;overflow:hidden}
body{position:relative;background:var(--white);font-family:"PT Sans",sans-serif;color:var(--text)}
.abs{position:absolute}

.sky{left:0;top:0;width:1055px;height:540px}

.nav-ribbon{left:65px;top:60px;width:925px;height:70px}
.nav{left:95px;top:72px;width:866px;height:51px;font-family:"Roboto Condensed",sans-serif;font-weight:700;font-size:16px;color:var(--white);letter-spacing:.3px}
.nav a{color:inherit;text-decoration:none;position:absolute;top:17px}
.brand{left:458px;top:28px;width:124px;height:124px;border-radius:50%;background:var(--white);border:3px solid var(--red)}
.brand-name{left:458px;top:80px;width:124px;text-align:center;font-family:"Roboto Condensed",sans-serif;font-weight:700;font-size:15px;color:var(--red)}

.hero-frame{left:95px;top:137px;width:864px;height:353px;background:rgba(255,255,255,.85);border-radius:4px}
.hero-photo{left:101px;top:145px;width:848px;height:336px;border-radius:3px;
  background:radial-gradient(ellipse 300px 220px at 600px 170px,#c98d45 0%,#b7823f 40%,rgba(140,170,40,0) 75%),linear-gradient(180deg,#a4c228 0%,#8db524 45%,#5f9a1e 100%)}
.hero-kicker{left:153px;top:226px;font-size:27px;color:var(--white)}
.hero-title{left:153px;top:258px;font-size:37px;color:var(--white)}
.hero-copy{left:157px;top:307px;width:310px;font-size:12.5px;line-height:18px;color:var(--white)}
.btn{display:flex;align-items:center;justify-content:center;color:var(--white);font-size:12.5px;border-radius:3px;text-decoration:none}
.btn-green{background:linear-gradient(#8cb33a,#66891d);box-shadow:0 1px 2px rgba(0,0,0,.25)}
.btn-blue{background:linear-gradient(#52b0cc,#3188a5);box-shadow:0 1px 2px rgba(0,0,0,.25)}
.hero-btn{left:156px;top:351px;width:91px;height:26px}
.dots{left:157px;top:395px;display:flex;gap:3px}
.dots span{width:11px;height:11px;border-radius:50%;background:rgba(255,255,255,.35)}
.dots span:first-child{background:var(--white)}

.welcome-title{left:105px;top:568px;font-size:26px;color:var(--heading);font-weight:400}
.welcome-copy{left:107px;top:603px;width:570px;font-size:11.4px;line-height:18.6px}
.welcome-copy p+p{margin-top:8px}
.welcome-btn{left:105px;top:733px;width:90px;height:27px}

.card-photo{top:798px;width:177px;height:98px}
.card-title{top:902px;font-size:19.5px;color:var(--green-title)}
.card-copy{top:929px;width:185px;font-size:10.3px;line-height:18.6px;color:#8a8a8a;white-space:nowrap}
.card-btn{width:91px;height:27px}

.form-box{left:707px;top:560px;width:251px;height:302px;border-radius:4px;overflow:hidden;background:linear-gradient(#e52b1e,#c8170f);box-shadow:0 1px 2px rgba(0,0,0,.2)}
.form-head{left:0;top:0;width:251px;height:50px}
.form-title{left:0;top:14px;width:251px;text-align:center;font-size:21px;color:var(--maroon);font-weight:700;letter-spacing:-.2px}
.field{left:21px;width:214px;height:23px;background:var(--white);border-radius:2px;font-size:10.5px;color:#7a7a7a;padding:5px 9px}
.field-msg{height:56px}
.submit{left:173px;top:266px;width:63px;height:25px;background:#a3120b;border-radius:2px;color:var(--white);font-size:13px;display:flex;align-items:center;justify-content:center}

.package{left:707px;top:870px;width:251px;height:141px;border-radius:3px;background:linear-gradient(#fde25a,var(--yellow) 40%,var(--yellow-deep));box-shadow:0 1px 2px rgba(0,0,0,.2)}
.package-title{left:25px;top:17px;font-size:21px;color:var(--maroon);font-weight:400}
.package-list{list-style:none;font-size:12.3px;color:var(--maroon);line-height:20px}
.package-list li{position:relative;padding-left:9px}
.package-list li::before{content:"";position:absolute;left:0;top:6px;border-left:4px solid var(--maroon);border-top:4px solid transparent;border-bottom:4px solid transparent}

.footer{left:0;top:1095px;width:1055px;height:105px;background:var(--footer-bg);border-top:1px solid #d3e7ef}
.footer-nav{left:95px;top:30px;font-family:"Roboto Condensed",sans-serif;font-weight:500;font-size:12px;color:var(--footer-link);word-spacing:1px}
.footer-nav span{margin:0 4px;color:#7fa6b6}
.copyright{left:95px;top:60px;font-size:11px;color:#6f8c98}
.social{left:853px;top:31px;display:flex;gap:7px}
.social span{width:21px;height:21px;border-radius:2px;background:#6fa0b4}
</style>
</head>
<body>

<svg class="abs sky" viewBox="0 0 1055 540" aria-hidden="true">
  <defs>
    <linearGradient id="skyFill" x1="0" y1="0" x2="0" y2="1">
      <stop offset="0" stop-color="#e6f7fd"/>
      <stop offset="1" stop-color="#cdeefa"/>
    </linearGradient>
  </defs>
  <path d="M0 0H1055V470C900 505 700 540 420 525C240 515 90 500 0 515Z" fill="url(#skyFill)"/>
</svg>

<svg class="abs nav-ribbon" viewBox="0 0 925 70" aria-hidden="true">
  <polygon points="0,5 47,5 47,57 0,57 18,31" fill="#b7160f"/>
  <polygon points="925,5 878,5 878,57 925,57 907,31" fill="#b7160f"/>
  <rect x="30" y="12" width="866" height="51" fill="#e1251b"/>
  <rect x="30" y="12" width="866" height="4" fill="#f0493d"/>
</svg>

<nav class="abs nav">
  <a style="left:28px">HOME</a>
  <a style="left:98px">ABOUT US</a>
  <a style="left:196px">SERVICES</a>
  <a style="left:290px">BLOG</a>
  <a style="left:526px">RENT A HEN</a>
  <a style="left:637px">PACKAGES</a>
  <a style="left:739px">CONTACT</a>
</nav>
<div class="abs brand"></div>
<div class="abs brand-name">Lease-My-Goose</div>

<div class="abs hero-frame"></div>
<div class="abs hero-photo" role="img" aria-label="Photograph of a brown hen walking on green grass"></div>
<div class="abs hero-kicker">We Provide Seasonal</div>
<div class="abs hero-title">Rentals of Hens in US..</div>
<div class="abs hero-copy">Class aptent taciti sociosqu ad litora torquent per conubia nostra per inceptos hymenaeos Proin nulla</div>
<a class="abs btn btn-green hero-btn">Learn More</a>
<div class="abs dots"><span></span><span></span><span></span><span></span></div>

<h1 class="abs welcome-title">Welcome to Our Website Mainpage..</h1>
<div class="abs welcome-copy">
  <p>Vivamus porttitor, g, purus nisi eleifend libero, a tempus libero lectus feugiat felis. Morbi diam mauris, viverra in, gravida eu, mattis in, ante. Morbi eget arcu. Morbi porta, libero id ullamcorper nonummy, nibh ligula pulvinar metus, eget consectetuer augue nisi quis lacus.</p>
  <p>Ut ac mi quis lacus mollis aliquam. Curabitur iaculis tempus eros. Curabitur vel mi sit amet magna malesuada ultrices. Ut nisi erat, fermentum vel, congue id, euismod in, elit. Fusce ultricies, orci ac feugiat suscipit, leo massa sodales velit, et scelerisque mi tortor at ipsum.</p>
</div>
<a class="abs btn btn-blue welcome-btn">Learn More</a>

<div class="abs card-photo" style="left:106px;background:linear-gradient(135deg,#b9772e,#7e6a4e 50%,#9aa07a)" role="img" aria-label="Photograph of two hens beside a wire fence"></div>
<div class="abs card-title" style="left:109px">Rent a Hen</div>
<div class="abs card-copy" style="left:109px">Praesent elementum elit at tellus.<br>nec, ultricies sit amet, porttitor mattis,<br>enim. In massa libero, interdum nec,<br>interdum vel, blandit</div>
<a class="abs btn btn-green card-btn" style="left:111px;top:1017px">Learn More</a>

<div class="abs card-photo" style="left:299px;background:linear-gradient(135deg,#c98040,#a5582a 50%,#d9a36a)" role="img" aria-label="Photograph of a flock of brown hens feeding"></div>
<div class="abs card-title" style="left:299px">Rent a Hen</div>
<div class="abs card-copy" style="left:299px">Praesent elementum elit at tellus.<br>nec, ultricies sit amet, porttitor mattis,<br>enim. In massa libero, interdum nec,<br>interdum vel, blandit</div>
<a class="abs btn btn-green card-btn" style="left:297px;top:1013px">Learn More</a>

<div class="abs card-photo" style="left:493px;background:linear-gradient(135deg,#3a3a36,#6b5a48 50%,#5f7a3a)" role="img" aria-label="Photograph of a hen standing in a farmyard"></div>
<div class="abs card-title" style="left:494px">Rent a Hen</div>
<div class="abs card-copy" style="left:494px">Praesent elementum elit at tellus.<br>nec, ultricies sit amet, porttitor mattis,<br>enim. In massa libero, interdum nec,<br>interdum vel, blandit</div>
<a class="abs btn btn-green card-btn" style="left:491px;top:1013px">Learn More</a>

<form class="abs form-box">
  <svg class="abs form-head" viewBox="0 0 251 50" aria-hidden="true">
    <path d="M0 0H251V45Q125 55 0 45Z" fill="#fbd92b"/>
  </svg>
  <div class="abs form-title">Fill Our Contact Form</div>
  <div class="abs field" style="top:60px">First Name</div>
  <div class="abs field" style="top:88px">Last Name</div>
  <div class="abs field" style="top:116px">Zip code</div>
  <div class="abs field" style="top:144px">Phone no. (optional)</div>
  <div class="abs field" style="top:172px">Email address</div>
  <div class="abs field field-msg" style="top:200px">Message</div>
  <div class="abs submit">Submit</div>
</form>

<section class="abs package">
  <h2 class="abs package-title">Package Inculdes</h2>
  <ul class="abs package-list" style="left:25px;top:55px">
    <li>Two hens</li><li>Coop</li><li>Attached run</li>
  </ul>
  <ul class="abs package-list" style="left:120px;top:55px">
    <li>Feeder</li><li>Waterer and food.</li>
  </ul>
</section>

<footer class="abs footer">
  <div class="abs footer-nav">HOME<span>|</span>ABOUT US<span>|</span>SERVICES<span>|</span>BLOG<span>|</span>RENT A HEN<span>|</span>PACKAGES<span>|</span>CONTACT</div>
  <div class="abs copyright">Copyright © 2013 Company Name.&nbsp; All right reserved</div>
  <div class="abs social"><span></span><span></span><span></span><span></span></div>
</footer>

</body>
</html>
```